Qolvar Energy Information Site Redesign

Re-vamp current site at qolvarenergy.com to include new logo, verbiage updates as needed, redesign, etc. Company overview and additional information on current QVR url.

```html
<!DOCTYPE html>
<html lang="en">
<head>
<meta charset="utf-8">
<title>Qolvar Energy Information</title>
<link href="https://fonts.googleapis.com/css2?family=Montserrat:wght@400;500;600;700&family=Open+Sans:wght@400;600&display=swap" rel="stylesheet">
<style>
:root{
  --orange:#f5921f;
  --orange-dark:#e07f10;
  --blue:#1a6cb3;
  --blue-deep:#125a9b;
  --ink:#222;
  --text:#555;
  --line:#e3e3e3;
  --footer:#1c1c1c;
  --white:#fff;
}
*{margin:0;padding:0;box-sizing:border-box}
html,body{width:1200px;height:3516px;overflow:hidden}
body{position:relative;background:var(--white);font-family:"Open Sans",Arial,sans-serif;color:var(--text)}
.abs{position:absolute}
/* top bar */
.topbar{left:352px;top:0;width:848px;height:42px;background:var(--blue);border-bottom-left-radius:34px;display:flex;align-items:center;gap:48px;padding-left:70px;color:var(--white);font-size:13px}
.topbar span{display:flex;align-items:center;gap:10px}
.header{left:0;top:42px;width:1200px;height:75px}
.brand{left:74px;top:60px;display:flex;align-items:center;gap:10px;font-family:"Montserrat",sans-serif;font-weight:700;font-size:22px;color:var(--blue)}
.brand i{width:30px;height:30px;border-radius:50%;background:var(--orange);display:block}
.nav{right:76px;top:68px;display:flex;gap:28px;font-family:"Montserrat",sans-serif;font-size:13px;font-weight:500;color:#333}
.nav .active{color:var(--blue)}
/* hero */
.hero-photo{left:0;top:117px;width:1200px;height:680px;background:linear-gradient(100deg,#2b3440 0%,#4a5562 35%,#6c6f70 55%,#b97a3a 75%,#d88f2e 88%,#6b5a48 100%)}
.hero-shade{left:0;top:117px;width:1200px;height:680px;background:rgba(20,28,40,.35)}
.hero-title{left:0;top:383px;width:1200px;text-align:center;font-family:"Montserrat",sans-serif;font-weight:700;font-size:40px;color:var(--orange);letter-spacing:.5px}
.hero-sub{left:300px;top:452px;width:600px;text-align:center;font-size:17px;line-height:30px;color:var(--white)}
.bands{left:0;top:0;width:1200px;height:3516px}
/* diagram */
.node{width:142px;height:142px;border-radius:50%;background:var(--white);border:4px solid var(--orange);box-shadow:0 0 0 4px var(--white);display:flex;align-items:center;justify-content:center;transform:translate(-50%,-50%)}
.node-ring{width:122px;height:122px;border-radius:50%;border:3px solid var(--blue);display:flex;align-items:center;justify-content:center}
.hub{left:600px;top:844px;width:258px;height:258px;border-radius:50%;background:var(--white);transform:translate(-50%,-50%);display:flex;align-items:center;justify-content:center;font-family:"Montserrat",sans-serif;font-weight:700;font-size:44px;color:var(--blue)}
.hub i{position:absolute;width:190px;height:190px;border-radius:50%;border:3px solid var(--blue);opacity:.25}
.label{font-family:"Montserrat",sans-serif;font-weight:500;font-size:18px;line-height:27px;color:var(--white)}
/* welcome */
.about-photo{left:134px;top:1411px;width:412px;height:412px;border-radius:50%;background:radial-gradient(circle at 50% 30%,#f3c59a 0%,#8a7fa8 40%,#2c3f70 75%,#1a2a4c 100%)}
.about-photo-small{left:78px;top:1660px;width:196px;height:196px;border-radius:50%;border:6px solid var(--white);background:linear-gradient(135deg,#cfe3f2,#6f9fc6 60%,#2d5c8c)}
.welcome-title{left:619px;top:1470px;font-family:"Montserrat",sans-serif;font-weight:600;font-size:40px;color:var(--blue)}
.welcome-copy{left:619px;top:1540px;width:500px;font-size:13px;line-height:24px}
.welcome-copy p+p{margin-top:12px}
.btn{left:619px;top:1752px;width:188px;height:50px;border-radius:14px;background:var(--blue);color:var(--white);font-family:"Montserrat",sans-serif;font-weight:600;font-size:16px;display:flex;align-items:center;justify-content:center}
/* testimonials */
.section-title{left:0;width:1200px;text-align:center;font-family:"Montserrat",sans-serif;font-weight:500}
.testi-title{top:2030px;font-size:40px;color:var(--white)}
.avatar{left:537px;top:2112px;width:126px;height:126px;border-radius:50%;background:linear-gradient(160deg,#c9d3dc,#7d8a99 60%,#2a3542);border:4px solid var(--white)}
.quote{left:520px;top:2112px;width:46px;height:46px;border-radius:50%;background:var(--blue);border:3px solid var(--white);color:var(--white);font-family:Georgia,serif;font-size:34px;font-weight:700;display:flex;align-items:center;justify-content:center;line-height:1;padding-top:12px}
.testi-name{top:2270px;font-size:17px;font-weight:600;color:var(--white)}
.testi-text{left:240px;top:2312px;width:720px;text-align:center;font-size:13px;line-height:23px;color:var(--white)}
.dots{left:552px;top:2416px;display:flex;gap:6px}
.dots i{width:18px;height:18px;border-radius:50%;border:2px solid var(--white);display:block}
.dots i.on{background:var(--white);box-shadow:inset 0 0 0 3px var(--blue)}
/* clients */
.clients-title{top:2556px;font-size:25px;line-height:35px;color:var(--ink)}
.clients{left:66px;top:2658px;width:1071px;display:grid;grid-template-columns:repeat(5,1fr);grid-template-rows:96px 96px}
.client{display:flex;align-items:center;justify-content:center;gap:8px;font-family:"Montserrat",sans-serif;font-weight:700;font-size:15px;color:#2f3b48;border-right:1px solid var(--line);border-bottom:1px solid var(--line)}
.client:nth-child(5n){border-right:none}
.client:nth-child(n+6){border-bottom:none}
.client b{width:12px;height:12px;background:var(--orange);display:block}
.pager{left:541px;top:2896px;display:flex;gap:4px}
.pager i{width:36px;height:3px;background:#cfe0ef;display:block}
.pager i.on{background:var(--blue)}
/* contact */
.contact-title{top:3060px;font-size:40px;color:var(--white)}
.contact-sub{top:3124px;font-size:16px;color:var(--white);font-family:"Open Sans",sans-serif;font-weight:400}
.field{height:47px;border:1.5px solid rgba(255,255,255,.85);border-radius:16px;color:var(--white);font-size:13px;padding:14px 24px}
.send{left:938px;top:3320px;width:60px;height:60px;border-radius:50%;background:var(--white);display:flex;align-items:center;justify-content:center}
.footer{left:0;top:3446px;width:1200px;height:70px;background:var(--footer);color:#ddd;font-size:13px;display:flex;align-items:center;justify-content:center}
</style>
</head>
<body>

<div class="abs topbar">
  <span><svg width="12" height="16" viewBox="0 0 12 16"><path d="M6 0a6 6 0 0 1 6 6c0 4-6 10-6 10S0 10 0 6a6 6 0 0 1 6-6z" fill="#fff"/><circle cx="6" cy="6" r="2.2" fill="#1a6cb3"/></svg>415 Larkspur Ave. Suite 210 Austin, TX 78704</span>
  <span><svg width="14" height="14" viewBox="0 0 14 14"><path d="M3 0l3 3-2 2c1 2 3 4 5 5l2-2 3 3-2 3C6 14 0 8 0 3z" fill="#fff"/></svg>800-555-0142</span>
  <span><svg width="16" height="12" viewBox="0 0 16 12"><rect width="16" height="12" rx="1" fill="#fff"/><path d="M0 1l8 6 8-6" stroke="#1a6cb3" stroke-width="1.5" fill="none"/></svg>support@qolvarenergy.com</span>
</div>
<div class="abs brand"><i></i>QOLVARENERGY</div>
<nav class="abs nav"><span class="active">HOME</span><span>WHAT WE DO</span><span>ABOUT QVR</span><span>BLOG</span><span>CONTACT</span></nav>

<div class="abs hero-photo" role="img" aria-label="Engineer in hard hat and safety vest holding a laptop at an industrial site"></div>
<div class="abs hero-shade"></div>
<h1 class="abs hero-title">QOLVAR ENERGY INFORMATION</h1>
<p class="abs hero-sub">QVR provides the technology to efficiently transfer information electronically and access, integrate and manage data.</p>

<svg class="abs bands" viewBox="0 0 1200 3516" aria-hidden="true">
  <path d="M0 780 C300 760 520 720 760 722 C950 724 1100 750 1200 762 L1200 1420 C900 1390 300 1390 0 1420 Z" fill="var(--orange)"/>
  <path d="M0 1900 C300 1960 900 1960 1200 1900 L1200 2508 L0 2508 Z" fill="var(--blue)"/>
  <path d="M0 3050 C300 2990 700 2970 1200 3000 L1200 3446 L0 3446 Z" fill="var(--orange)"/>
  <g stroke="#fff" stroke-width="5">
    <line x1="600" y1="844" x2="323" y2="902"/>
    <line x1="600" y1="844" x2="434" y2="1036"/>
    <line x1="600" y1="844" x2="600" y2="1130"/>
    <line x1="600" y1="844" x2="755" y2="1036"/>
    <line x1="600" y1="844" x2="879" y2="902"/>
  </g>
</svg>

<div class="abs hub"><i></i>QVR</div>

<div class="abs node" style="left:323px;top:902px"><div class="node-ring">
  <svg width="56" height="56" viewBox="0 0 56 56" fill="none" stroke="var(--orange)" stroke-width="2.5"><rect x="6" y="8" width="40" height="11" rx="2"/><rect x="6" y="22" width="40" height="11" rx="2"/><rect x="6" y="36" width="40" height="11" rx="2"/><circle cx="46" cy="44" r="7" fill="#fff"/></svg>
</div></div>
<div class="abs node" style="left:434px;top:1036px"><div class="node-ring">
  <svg width="56" height="56" viewBox="0 0 56 56" fill="none" stroke="var(--orange)" stroke-width="2.5"><rect x="4" y="8" width="26" height="14" rx="2"/><rect x="26" y="34" width="26" height="14" rx="2"/><path d="M38 12h10v16M44 24l4 4 4-4M18 44H8V28M4 32l4-4 4 4"/></svg>
</div></div>
<div class="abs node" style="left:600px;top:1130px"><div class="node-ring">
  <svg width="56" height="56" viewBox="0 0 56 56" fill="none" stroke="var(--orange)" stroke-width="2.5"><path d="M8 6h20l6 6v22H8z"/><path d="M24 22h18l6 6v22H24z"/><path d="M30 34h12M30 40h12"/></svg>
</div></div>
<div class="abs node" style="left:755px;top:1036px"><div class="node-ring">
  <svg width="56" height="56" viewBox="0 0 56 56" fill="none" stroke="var(--orange)" stroke-width="2.5"><path d="M6 16h44v8a4 4 0 0 0 0 8v8H6v-8a4 4 0 0 0 0-8z"/><path d="M18 16v24" stroke-dasharray="3 3"/><path d="M24 26h18M24 32h12"/></svg>
</div></div>
<div class="abs node" style="left:879px;top:902px"><div class="node-ring">
  <svg width="56" height="56" viewBox="0 0 56 56" fill="none" stroke="var(--orange)" stroke-width="2.5"><path d="M4 20l10-8 10 6 8-6 10 4 10 6"/><path d="M14 12v16l12 12 16-14"/><path d="M24 24l10 10M30 20l10 10"/></svg>
</div></div>

<div class="abs label" style="left:66px;top:916px;text-align:right;width:170px">Data Management<br>Solutions</div>
<div class="abs label" style="left:156px;top:1064px">Well Data Exchange</div>
<div class="abs label" style="left:494px;top:1231px">Partner Data Exchange</div>
<div class="abs label" style="left:852px;top:1064px">E-Ticket Exchange</div>
<div class="abs label" style="left:972px;top:916px">Owner Relations<br>Services</div>

<div class="abs about-photo" role="img" aria-label="City skyline at dusk with glowing network lines"></div>
<div class="abs about-photo-small" role="img" aria-label="Hands typing on a laptop"></div>
<h2 class="abs welcome-title">Welcome to QVR</h2>
<div class="abs welcome-copy">
  <p>Qolvar Energy Information has been providing electronic exchange solutions for the energy industry for over 20 years. QVR utilizes proven data integration techniques to provide customers with cost effective methods to efficiently access, transform and distribute their data. Our customer list includes over 95% of the Fortune 500 energy companies.</p>
  <p>Our company was founded in 1991, and established itself as the sole provider of audited crude oil pricing data to the oil industry.</p>
</div>
<div class="abs btn">KNOW MORE</div>

<h2 class="abs section-title testi-title">Testimonials</h2>
<div class="abs avatar" role="img" aria-label="Portrait of a client giving a testimonial"></div>
<div class="abs quote">“</div>
<div class="abs section-title testi-name">- NAME SURNAME</div>
<p class="abs testi-text">Lorem Ipsum is simply dummy text of the printing and typesetting industry. Lorem Ipsum has been the industry's standard dummy text ever since the 1500s, when an unknown printer took a galley of type and scrambled it to make a type specimen book. It has survived not only five centuries.</p>
<div class="abs dots"><i class="on"></i><i></i><i></i><i></i></div>

<h2 class="abs section-title clients-title">Want to see what QVR Energy can do for your company?<br>Visit some of our client-branded customer and owner relations websites</h2>
<div class="abs clients">
  <div class="client"><b></b>Redmesa Holdings, LP</div>
  <div class="client">Tellurin Energy, L.P.</div>
  <div class="client">Ocotillo</div>
  <div class="client">Verdana Oil</div>
  <div class="client">Barlow Ridge</div>
  <div class="client">Ascendra</div>
  <div class="client">Coyote Flats</div>
  <div class="client">Marrow Creek</div>
  <div class="client">Pecan Bluff</div>
  <div class="client">Alder Resources</div>
</div>
<div class="abs pager"><i class="on"></i><i></i><i></i></div>

<h2 class="abs section-title contact-title">Contact us</h2>
<p class="abs section-title contact-sub">For more information on our services please feel free to contact us.</p>
<div class="abs field" style="left:145px;top:3183px;width:293px">Name</div>
<div class="abs field" style="left:455px;top:3183px;width:290px">Email</div>
<div class="abs field" style="left:762px;top:3183px;width:290px">Phone</div>
<div class="abs field" style="left:145px;top:3246px;width:907px;height:102px">Message</div>
<div class="abs send"><svg width="26" height="24" viewBox="0 0 26 24"><path d="M0 0l26 12L0 24l4-12z" fill="var(--orange)"/></svg></div>

<footer class="abs footer">2018 ©QOLVARENERGY. - All Rights Reserved</footer>
</body>
</html>
```